Design einer Preisliste
Zielgruppe
Wir produzieren und verkaufen Suppen Konserven und Konzentrate an Gewerbetreibende + Endabnehmer.
Wir sind im Premium Segment angesiedelt.
Hauptsächlicher Vertrieb erfolgt über den Großhandel
Die Firma ist über 80 Jahre alt
https://www.morvak-eintopf.de/
Aufgabenstellung
Unsere Preisliste soll neu designed werden.
Vorgaben sind:
Hochwertig + Elegant
Eher konservativ gehalten als zu bunt.
Die neuen Preise müssen in die Liste mit eingepflegt werden
Die alte Preisliste und die neuen Preise werden mit beigefügt.

```html
<!DOCTYPE html>
<html lang="de">
<head>
<meta charset="utf-8">
<title>morvak Sortimentliste 3/4</title>
<link href="https://fonts.googleapis.com/css2?family=Montserrat:wght@400;500;600;700&display=swap" rel="stylesheet">
<style>
:root{
  --ink:#3a3a3a;
  --dark:#4a4a48;
  --gold:#b89a54;
  --row-a:#efe8dd;
  --row-b:#f8f6f2;
  --green:#4caf3f;
  --salmon:#ec8a72;
  --red:#e3231b;
  --brand:#d9241c;
}
*{margin:0;padding:0;box-sizing:border-box}
html,body{width:848px;height:1200px;overflow:hidden;background:#fff}
body{position:relative;font-family:'Montserrat',sans-serif;color:var(--ink)}
.page-head{position:absolute;top:18px;right:0;height:26px;display:flex;align-items:center}
.brand{display:flex;align-items:center;gap:5px;font-weight:700;font-size:15px;color:var(--brand);margin-right:8px}
.brand-dot{width:9px;height:9px;border-radius:50%;background:var(--brand)}
.doc-title{font-size:10px;color:var(--gold);margin-right:8px;letter-spacing:.1px}
.doc-title b{font-weight:600}
.page-no{background:var(--gold);color:#fff;width:115px;height:26px;display:flex;align-items:center;justify-content:center;font-size:14px;font-weight:500;letter-spacing:1px}
.section-bar{position:absolute;left:0;width:336px;height:38px;background:var(--dark);color:#fff;font-weight:600;font-size:17px;letter-spacing:-.1px;display:flex;align-items:center;padding-left:61px;white-space:nowrap}
.tag{position:absolute;left:342px;height:38px;color:#fff;font-weight:600;font-size:13px;display:flex;align-items:center;padding:0 9px}
.tag-veg{background:var(--green);width:137px}
.tag-sea{background:var(--salmon);width:72px}
.note{position:absolute;left:345px;font-size:8.5px}
table{position:absolute;left:60px;width:728px;border-collapse:collapse;table-layout:fixed}
th{font-size:8px;font-weight:700;line-height:10px;padding-bottom:2px;border-bottom:1.5px solid var(--gold);text-align:center;vertical-align:bottom}
td{height:26.3px;font-size:8.6px;text-align:center;border-right:2px solid #fff;white-space:nowrap}
td:last-child{border-right:0}
tbody tr:nth-child(odd) td{background:var(--row-a)}
tbody tr:nth-child(even) td{background:var(--row-b)}
td.name{text-align:left;padding-left:9px;font-size:12px;font-weight:600}
.name small{font-size:8.5px;font-weight:400;margin-left:4px}
.name em{font-style:normal;font-weight:400;color:var(--gold)}
.footer-note{position:absolute;left:469px;top:1155px;width:379px;height:26px;background:var(--red);color:#fff;font-size:7.8px;font-weight:600;display:flex;align-items:center;padding-left:9px}
</style>
</head>
<body>
<header class="page-head">
  <div class="brand"><span class="brand-dot"></span>morvak</div>
  <div class="doc-title"><b>GROSSVERBRAUCHER</b> | Sortimentliste</div>
  <div class="page-no">3 / 4</div>
</header>

<div class="section-bar" style="top:60px">Einzelportion Ringpull-Dosen</div>
<div class="note" style="top:78px">auch in 24/4 Kartons erhältlich</div>
<table style="top:108px">
<colgroup><col style="width:332px"><col style="width:46px"><col style="width:66px"><col style="width:59px"><col style="width:44px"><col style="width:67px"><col style="width:65px"><col style="width:49px"></colgroup>
<thead><tr><th>Artikel-<br>bezeichnung</th><th>morvak-<br>Nr.</th><th>Dosengröße<br>je Artikel</th><th>Inhalt<br>Dose</th><th>Euro<br>Dose</th><th>Karton<br>Inhalt</th><th>C+C Einheit<br>EAN 40817-</th><th>Preis €<br>Karton</th></tr></thead>
<tbody>
<tr><td class="name">Hühnersuppe Klar <em>First Class</em></td><td>301-1</td><td>1/4 Dose</td><td>212 ml</td><td>1,40</td><td>50 = 10 x 5</td><td>00 51120 3</td><td>70,00</td></tr>
<tr><td class="name">Rindsuppe<small>mit Eierstich &amp; Nudeln</small></td><td>302-1</td><td>1/4 Dose</td><td>212 ml</td><td>1,40</td><td>50 = 10 x 5</td><td>00 51210 8</td><td>70,00</td></tr>
<tr><td class="name">Hühnersuppe<small>mit Prinzessudeln</small></td><td>303-1</td><td>1/4 Dose</td><td>212 ml</td><td>1,40</td><td>50 = 10 x 5</td><td>00 51330 5</td><td>70,00</td></tr>
<tr><td class="name">Hühnersuppe<small>mit Eierstich &amp; Reis</small></td><td>304-1</td><td>1/4 Dose</td><td>212 ml</td><td>1,40</td><td>50 = 10 x 5</td><td>00 51440 1</td><td>70,00</td></tr>
<tr><td class="name">Tomatensuppe<small>mit Fleischklößchen &amp; Reis</small></td><td>305-1</td><td>1/4 Dose</td><td>212 ml</td><td>1,40</td><td>50 = 10 x 5</td><td>00 51550 7</td><td>70,00</td></tr>
<tr><td class="name">Serb. Bohnensuppe <em>de Luxe</em><small>mit Fleischklößchen &amp; Reis</small></td><td>306-1</td><td>1/4 Dose</td><td>212 ml</td><td>1,40</td><td>50 = 10 x 5</td><td>00 51660 4</td><td>70,00</td></tr>
<tr><td class="name">Geb. Ochsenschwanz<small>mit doppelte Einlage</small></td><td>307-1</td><td>1/4 Dose</td><td>212 ml</td><td>1,40</td><td>50 = 10 x 5</td><td>00 51770 9</td><td>70,00</td></tr>
<tr><td class="name">Gulaschsuppe<small>mit doppelte Einlage</small></td><td>308-1</td><td>1/4 Dose</td><td>212 ml</td><td>1,40</td><td>50 = 10 x 5</td><td>00 51880 6</td><td>70,00</td></tr>
<tr><td class="name">Kessel Gulasch-Suppe</td><td>309-1</td><td>1/4 Dose</td><td>212 ml</td><td>1,40</td><td>50 = 10 x 5</td><td>00 52110 2</td><td>70,00</td></tr>
<tr><td class="name">Grüne Pfeffersuppe »Madagaskar«</td><td>310-1</td><td>1/4 Dose</td><td>212 ml</td><td>1,40</td><td>50 = 10 x 5</td><td>00 52220 8</td><td>70,00</td></tr>
<tr><td class="name">Markklößchensuppe <em>de Luxe</em></td><td>311-1</td><td>1/4 Dose</td><td>212 ml</td><td>1,40</td><td>50 = 10 x 5</td><td>00 52330 4</td><td>70,00</td></tr>
<tr><td class="name">Schwäbische Maultschen-Suppe</td><td>312-1</td><td>1/4 Dose</td><td>212 ml</td><td>1,40</td><td>50 = 10 x 5</td><td>00 52440 0</td><td>70,00</td></tr>
<tr><td class="name">Minestrone Capri<small>deftig rustikal</small></td><td>313-1</td><td>1/4 Dose</td><td>212 ml</td><td>1,50</td><td>50 = 10 x 5</td><td>00 52550 6</td><td>75,00</td></tr>
<tr><td class="name">Schlemmer Topf Huhn</td><td>314-1</td><td>1/4 Dose</td><td>212 ml</td><td>1,50</td><td>50 = 10 x 5</td><td>00 52660 3</td><td>75,00</td></tr>
<tr><td class="name">Schlemmer Topf Rind <em>First Class</em></td><td>315-1</td><td>1/4 Dose</td><td>212 ml</td><td>1,50</td><td>50 = 10 x 5</td><td>00 52770 8</td><td>75,00</td></tr>
<tr><td class="name">Leberknödel-Suppe</td><td>316-1</td><td>1/4 Dose</td><td>212 ml</td><td>1,50</td><td>50 = 10 x 5</td><td>00 52880 5</td><td>75,00</td></tr>
<tr><td class="name">Pifferling-Creme-Suppe <em>First Class</em></td><td>317-1</td><td>1/4 Dose</td><td>212 ml</td><td>1,75</td><td>50 = 10 x 5</td><td>00 53110 1</td><td>87,50</td></tr>
</tbody></table>

<div class="section-bar" style="top:628px">Einzelportion Ringpull-Dosen</div>
<div class="tag tag-veg" style="top:628px">100 % vegetarisch</div>
<table style="top:678px">
<colgroup><col style="width:332px"><col style="width:46px"><col style="width:66px"><col style="width:59px"><col style="width:44px"><col style="width:67px"><col style="width:65px"><col style="width:49px"></colgroup>
<thead><tr><th>Artikel-<br>bezeichnung</th><th>morvak-<br>Nr.</th><th>Dosengröße<br>je Artikel</th><th>Inhalt<br>Dose</th><th>Euro<br>Dose</th><th>Karton<br>Inhalt</th><th>C+C Einheit<br>EAN 40817-</th><th>Preis €<br>Karton</th></tr></thead>
<tbody>
<tr><td class="name">Broccoli-Creme-Suppe</td><td>318-1</td><td>1/4 Dose</td><td>212 ml</td><td>1,40</td><td>50 = 10 x 5</td><td>00 55120 9</td><td>70,00</td></tr>
<tr><td class="name">Möhren-Ingwer-Suppe</td><td>319-1</td><td>1/4 Dose</td><td>212 ml</td><td>1,40</td><td>50 = 10 x 5</td><td>00 55230 5</td><td>70,00</td></tr>
<tr><td class="name">Kürbis-Mango-Creme</td><td>320-1</td><td>1/4 Dose</td><td>212 ml</td><td>1,40</td><td>50 = 10 x 5</td><td>00 55340 2</td><td>70,00</td></tr>
<tr><td class="name">Fruchtige Tomatensuppe</td><td>321-1</td><td>1/4 Dose</td><td>212 ml</td><td>1,40</td><td>50 = 10 x 5</td><td>00 55450 7</td><td>70,00</td></tr>
<tr><td class="name">Klare Zwiebelsuppe</td><td>322-1</td><td>1/4 Dose</td><td>212 ml</td><td>1,40</td><td>50 = 10 x 5</td><td>00 55560 4</td><td>70,00</td></tr>
<tr><td class="name">Champignon-Creme-Suppe</td><td>323-1</td><td>1/4 Dose</td><td>212 ml</td><td>1,40</td><td>50 = 10 x 5</td><td>00 55670 0</td><td>70,00</td></tr>
<tr><td class="name">Tomaten-Creme <em>First Class</em></td><td>324-1</td><td>1/4 Dose</td><td>212 ml</td><td>1,40</td><td>50 = 10 x 5</td><td>00 55780 6</td><td>70,00</td></tr>
<tr><td class="name">Spargel-Creme-Suppe</td><td>325-1</td><td>1/4 Dose</td><td>212 ml</td><td>1,50</td><td>50 = 10 x 5</td><td>00 55890 3</td><td>75,00</td></tr>
</tbody></table>

<div class="section-bar" style="top:960px">Einzelportion Ringpull-Dosen</div>
<div class="tag tag-sea" style="top:960px">Seafood</div>
<table style="top:1009px">
<colgroup><col style="width:332px"><col style="width:46px"><col style="width:66px"><col style="width:59px"><col style="width:44px"><col style="width:67px"><col style="width:65px"><col style="width:49px"></colgroup>
<thead><tr><th>Artikel-<br>bezeichnung</th><th>morvak-<br>Nr.</th><th>Dosengröße<br>je Artikel</th><th>Inhalt<br>Dose</th><th>Euro<br>Dose</th><th>Karton<br>Inhalt</th><th>C+C Einheit<br>EAN 40817-</th><th>Preis €<br>Karton</th></tr></thead>
<tbody>
<tr><td class="name">Norwegische Lachs-Creme <em>de Luxe</em><small>aus Wildlachs-Filet</small></td><td>326-1</td><td>1/4 Dose</td><td>212 ml</td><td>1,80</td><td>50 = 10 x 5</td><td>00 58560 8</td><td>90,00</td></tr>
<tr><td class="name">Hummersuppe »Alaska«<small>mit einer Schere aus Krabbenfleisch</small></td><td>327-1</td><td>1/4 Dose</td><td>212 ml</td><td>1,80</td><td>50 = 10 x 5</td><td>00 58670 5</td><td>90,00</td></tr>
<tr><td class="name">Büsumer Krabbensuppe<small>mit 25 g Tiefsee-Krabben 1. Wahl</small></td><td>328-1</td><td>1/4 Dose</td><td>212 ml</td><td>1,90</td><td>50 = 10 x 5</td><td>00 58780 2</td><td>95,00</td></tr>
<tr><td class="name">Büsumer Krabbensuppe<small>mit 25 g Nordsee-Krabben 1. Wahl</small></td><td>329-1</td><td>1/4 Dose</td><td>212 ml</td><td>2,05</td><td>50 = 10 x 5</td><td>00 58890 1</td><td>102,50</td></tr>
</tbody></table>

<div class="footer-note">Alle unsere Produkte haben eine garantierte Restlaufzeit von 30 Monaten.</div>
</body>
</html>
```